I'm looking for strong image and design for the first book in a series titled "Bernard Whitcombe On A Voyage Through Our Convictions" subtitle "Finding a Footing in Living"; although it's about beliefs, I'm not look for an ethereal feel as the first book is about how our beliefs impact our actions and expectations. I'm a published philosopher and keen on branding my name for professional purposes hence the use of my name :) The book will initially be an e-book but I will follow up with a paperback soon afterwards. My website http://bernardwhitcombe-example.com/ may provide some help on me and my projects. Thanks, Bern

Target Market(s)

Graduates and corporate folk who tend to lose their way in the systems.

Logo Text

Bernard Whitcombe on Convictions

Font styles to use
Sans Serif

Colors

Designer to choose colors to be used in the design.

Requirements
Must have
• Needless to say, but impact.
Nice to have
• Strong colours
Should not have
• Religious imagery; the book is philosophical and leans into living in this world.

```html
<!DOCTYPE html>
<html lang="en">
<head>
<meta charset="utf-8">
<title>Bernard Whitcombe – A Voyage Through Our Convictions – Book Cover</title>
<link rel="stylesheet" href="https://fonts.googleapis.com/css2?family=Bebas+Neue&family=Playfair+Display:wght@400;500&display=swap">
<style>
  :root {
    --page-bg: #eeebee;
    --cover-bg: #ffffff;
    --ink: #141414;
    --band-blue: #4f84ad;
    --band-line: rgba(255, 255, 255, 0.35);
    --band-text: #ffffff;
    --sky-top: #6f6a8f;
    --sky-glow: #c9a99a;
    --mountain: #3b3a52;
    --water: #a78c9c;
  }
  html, body {
    margin: 0;
    padding: 0;
    width: 1200px;
    height: 1200px;
    overflow: hidden;
    background: var(--page-bg);
  }
  .stage {
    position: relative;
    width: 1200px;
    height: 1200px;
  }
  .book-cover {
    position: absolute;
    left: 288px;
    top: 100px;
    width: 624px;
    height: 1000px;
    background: var(--cover-bg);
    box-shadow: 0 6px 24px rgba(0, 0, 0, 0.12);
    overflow: hidden;
  }
  .author-name {
    position: absolute;
    top: 38px;
    left: 0;
    width: 100%;
    margin: 0;
    text-align: center;
    font-family: "Playfair Display", serif;
    font-weight: 500;
    font-size: 25px;
    letter-spacing: 0.18em;
    color: var(--ink);
  }
  .title-band {
    position: absolute;
    left: 0;
    top: 203px;
    width: 560px;
    height: 74px;
  }
  .book-title {
    position: absolute;
    top: 136px;
    left: 0;
    width: 100%;
    margin: 0;
    text-align: center;
    font-family: "Bebas Neue", sans-serif;
    font-weight: 400;
    font-size: 78px;
    line-height: 72px;
    color: var(--ink);
  }
  .book-title .on-band {
    color: var(--band-text);
  }
  .book-title span {
    display: block;
  }
  .subtitle-band {
    position: absolute;
    left: 0;
    top: 427px;
    width: 100%;
    height: 75px;
    background: var(--band-blue);
  }
  .subtitle-band::before,
  .subtitle-band::after {
    content: "";
    position: absolute;
    left: 0;
    width: 100%;
    height: 1px;
    background: var(--band-line);
  }
  .subtitle-band::before { top: 14px; }
  .subtitle-band::after { bottom: 12px; }
  .book-subtitle {
    margin: 0;
    line-height: 75px;
    text-align: center;
    font-family: "Playfair Display", serif;
    font-weight: 400;
    font-size: 28px;
    letter-spacing: 0.06em;
    color: var(--band-text);
  }
  .cover-photo {
    position: absolute;
    left: 0;
    top: 502px;
    width: 100%;
    height: 498px;
    background:
      linear-gradient(180deg,
        var(--sky-top) 0%,
        #9a8aa3 28%,
        var(--sky-glow) 48%,
        var(--mountain) 60%,
        var(--mountain) 68%,
        var(--water) 78%,
        #7d6b80 100%);
  }
</style>
</head>
<body>
  <main class="stage">
    <article class="book-cover">
      <p class="author-name">BERNARD WHITCOMBE</p>

      <svg class="title-band" viewBox="0 0 560 74" aria-hidden="true">
        <path d="M0 0 H548 L552 8 L546 16 L556 26 L549 38 L558 50 L548 62 L553 74 H0 Z" fill="var(--band-blue)"/>
        <line x1="0" y1="12" x2="548" y2="12" stroke="rgba(255,255,255,0.3)" stroke-width="1"/>
        <line x1="0" y1="63" x2="548" y2="63" stroke="rgba(255,255,255,0.3)" stroke-width="1"/>
      </svg>

      <h1 class="book-title">
        <span>A VOYAGE</span>
        <span class="on-band">THROUGH OUR</span>
        <span>CONVICTIONS</span>
      </h1>

      <div class="subtitle-band">
        <p class="book-subtitle">"FINDING A FOOTING IN LIVING"</p>
      </div>

      <div class="cover-photo" role="img" aria-label="Photograph of a lone figure standing at the end of a flooded wooden jetty on a lake at dusk, dark mountains behind and a starry, glowing nebula sky above"></div>
    </article>
  </main>
</body>
</html>
```